Keystone BRISK Repairs Business card

Keystone Motors is looking for a business card design for our detailing wing "Keystone BRISK Repairs"
The services offered are vehicle paintless dent repairs, vehicle detailing, scratch and bumper repairs & paint and alloy wheel repairs.
Ideally the card design should be sharp, neat and professional. We are not looking for a card with pictures of cars.
Our corporate colours are blues (as in the logo supplied) which may look good with water droplets in high res and perhaps one or two images leaking off the card. Dark blacks with electric blues perhaps.
Images may be of a spray gun (we use Torvanex), a rotary polisher (Quill WideStep) or similar objects used in the processes.

Industry/Entity Type

Paint

Contact Information for Business Card

Title: Keystone BRISK Repairs
Services: Bumper Repairs
Scratch/Paint Repairs
Paintless dent repairs
Alloy wheel repairs
Name: Martin K
Telephone: 0427195364
Email : martin@keystonemotors.com.au

Font styles to use
Sans Serif
Other font styles liked:

Colors
0355a3
3277b5
0792cd
cfdfed

Requirements
Must have
• The title - "Keystone BRISK Repairs" should be a focus on either the from or back of the card
Should not have
• Photographs of cars

```html
<!DOCTYPE html>
<html lang="en">
<head>
<meta charset="utf-8">
<title>Keystone BRISK Repairs – Business Card</title>
<link rel="stylesheet" href="https://fonts.googleapis.com/css2?family=Open+Sans:ital,wght@0,400;0,600;0,700;1,400&display=swap">
<style>
  :root {
    --backdrop: #e9e9eb;
    --card-black: #050505;
    --card-white: #fbfbfb;
    --silver: #c9c9cc;
    --navy: #0c1f5c;
    --title-blue: #0b7ac2;
    --band-blue: #0792cd;
    --ink: #1a2440;
    --white: #ffffff;
  }
  * { box-sizing: border-box; margin: 0; padding: 0; }
  html, body {
    width: 1200px; height: 768px; overflow: hidden;
    background: var(--backdrop);
    font-family: "Open Sans", Arial, sans-serif;
  }
  .canvas { position: relative; width: 1200px; height: 768px; }

  .card {
    position: absolute; top: 224px;
    width: 560px; height: 320px;
    box-shadow: 0 6px 18px rgba(0,0,0,.18);
    overflow: hidden;
  }

  /* front */
  .card-front { left: 30px; background: var(--card-black); }
  .front-name {
    position: absolute; left: 0; right: 0; top: 50%;
    transform: translateY(-50%);
    text-align: center;
    color: var(--silver); font-weight: 600; font-size: 32px;
    white-space: nowrap;
  }

  /* back */
  .card-back { left: 610px; background: var(--card-white); }
  .back-title {
    position: absolute; left: 150px; top: 26px;
    color: var(--title-blue); font-weight: 600; font-size: 21px;
    white-space: nowrap;
  }
  .services { position: absolute; left: 108px; top: 72px; color: var(--ink); }
  .services h2 { font-size: 13px; font-weight: 700; color: var(--navy); margin-bottom: 3px; }
  .services ul { list-style: none; font-size: 12.5px; line-height: 20px; }
  .services li::before { content: "»"; color: var(--band-blue); margin-right: 9px; font-weight: 700; }

  .back-name {
    position: absolute; right: 40px; top: 122px;
    color: var(--navy); font-weight: 600; font-size: 20px;
    white-space: nowrap;
  }

  .back-shapes { position: absolute; left: 0; bottom: 0; }
  .holder {
    position: absolute; left: 24px; bottom: 34px;
    color: var(--white); font-size: 13px; white-space: nowrap;
  }
  .holder strong { font-weight: 700; margin-right: 6px; }
  .holder em { font-style: italic; font-size: 11.5px; }

  .contacts {
    position: absolute; right: 18px; bottom: 16px;
    list-style: none; color: var(--white);
    font-size: 14.5px; line-height: 25px; text-align: right;
  }
  .contacts li { display: flex; align-items: center; justify-content: flex-end; gap: 10px; white-space: nowrap; }
  .contacts svg { width: 14px; height: 14px; fill: var(--title-blue); }
</style>
</head>
<body>
<main class="canvas">

  <section class="card card-front" aria-label="Card front">
    <p class="front-name">Keystone Motors</p>
  </section>

  <section class="card card-back" aria-label="Card back">
    <h1 class="back-title">Keystone BRISK Repairs</h1>

    <div class="services">
      <h2>Our Services:</h2>
      <ul>
        <li>Bumper Repairs</li>
        <li>Alloy wheel Repairs</li>
        <li>Scratch/Paint Repairs</li>
        <li>Paintless dent Repairs</li>
      </ul>
    </div>

    <p class="back-name">Keystone Motors</p>

    <svg class="back-shapes" width="560" height="320" viewBox="0 0 560 320" aria-hidden="true">
      <polygon points="0,250 270,250 250,320 0,320" fill="var(--band-blue)"/>
      <polygon points="265,215 560,215 560,320 230,320" fill="var(--navy)"/>
    </svg>

    <p class="holder"><strong>Martin K</strong><em>Managing Director</em></p>

    <ul class="contacts">
      <li>0427195364
        <svg viewBox="0 0 16 16"><path d="M3 1l3 3-1.5 2a9 9 0 0 0 5.5 5.5L12 10l3 3-2 2C7 15 1 9 1 3z"/></svg></li>
      <li>martin@keystonemotors.com.au
        <svg viewBox="0 0 16 16"><path d="M1 3h14v10H1z M2 4l6 5 6-5" fill="none" stroke="var(--title-blue)" stroke-width="1.6"/></svg></li>
      <li>www.keystonemotors.com.au
        <svg viewBox="0 0 16 16"><circle cx="8" cy="8" r="7"/><path d="M1 8h14M8 1c-3 4-3 10 0 14M8 1c3 4 3 10 0 14" fill="none" stroke="var(--navy)" stroke-width="1"/></svg></li>
    </ul>
  </section>

</main>
</body>
</html>
```